'WILD' eye catching Business Card Design / Logo for production company / TV host / adventurer

Hi there,

We are looking for a 'WILD' and exciting logo and double sided business card for our business "Red Kettle Productions".

Toby Harlan is an international television host, adventurer, author and inspirational public speaker.

We want to project Toby's talents onto his business card.

We are looking for a business card design that can carry over onto letter heads, emails etc. We want a design that is 'WILD', different and exciting.

Feel free to check out Toby's web site: www.redkettleproductions.example.nz to get a better understanding what he is about.

Please feel free to go completely 'WILD' on this project as we want something different with lots of WOW factors.

Thank you so much and we look forward to your designs.

We have a feeling that there will be many more designs in the near future.

Best regards,

the production team

We have added another task to the list.

If the winning designer can also provide us with a matching letterhead and email signature based on the same style of design as the business card.

Target Market(s)

People with passion.

Industry/Entity Type

Business

Requirements
Must have
• Red Kettle Productions
Toby Harlan
14 Salt Marsh Lane
Ferncliff 7422
New Zealand

Phone +64-(0)3-5207 641
Cell +64-(0)274-615 203

email: redkettlenz@mailbox.example
www.redkettleprouctions.example.nz
Nice to have
• A feature made out of the name 'Red Kettle Productions'.

Toby Harlan's name reasonably obvious.

All other details (except web site) can be quite small.

```html
<!DOCTYPE html>
<html lang="en">
<head>
<meta charset="utf-8">
<title>Red Kettle Productions – Business Card</title>
<link rel="stylesheet" href="https://fonts.googleapis.com/css2?family=Chakra+Petch:ital,wght@0,700;1,700&display=swap">
<style>
  :root {
    --card-bg: #ffffff;
    --ink: #111111;
    --brand-grey: #4a4a4a;
    --brand-green: #5aa51c;
    --band-orange: #ff6a13;
    --band-edge: #ffffff;
  }
  html, body {
    margin: 0;
    padding: 0;
    overflow: hidden;
    background: var(--card-bg);
  }
  .card {
    position: relative;
    width: 1200px;
    height: 678px;
    overflow: hidden;
    background: var(--card-bg);
    font-family: "Chakra Petch", sans-serif;
    font-weight: 700;
    text-transform: uppercase;
  }
  .brand {
    position: absolute;
    left: 40px;
    top: 36px;
    display: flex;
    align-items: center;
    gap: 22px;
  }
  .brand-dot {
    width: 150px;
    height: 150px;
    border-radius: 50%;
    background: var(--brand-green);
    flex: none;
  }
  .brand-name {
    margin: 0;
    color: var(--brand-grey);
    font-size: 62px;
    line-height: 0.95;
    letter-spacing: 1px;
    font-style: normal;
  }
  .contact {
    position: absolute;
    left: 325px;
    top: 190px;
    margin: 0;
    color: var(--ink);
    font-style: italic;
    font-size: 31px;
    line-height: 43px;
    letter-spacing: 2px;
  }
  .contact p { margin: 0; }
  .contact .gap { height: 43px; }
  .contact .email { text-transform: uppercase; }
  .website {
    position: absolute;
    left: 44px;
    top: 600px;
    margin: 0;
    color: var(--brand-green);
    font-style: italic;
    font-size: 40px;
    letter-spacing: 0.5px;
  }
  .name-band {
    position: absolute;
    inset: 0;
  }
  .band-name {
    position: absolute;
    left: 1140px;
    top: 339px;
    transform: translate(-50%, -50%) rotate(90deg) skewX(-6deg);
    color: var(--band-edge);
    font-style: italic;
    font-size: 68px;
    letter-spacing: 4px;
    white-space: nowrap;
    margin: 0;
  }
</style>
</head>
<body>
  <div class="card">
    <div class="brand">
      <span class="brand-dot"></span>
      <p class="brand-name">Red Kettle<br>Productions</p>
    </div>

    <address class="contact">
      <p>Toby Harlan</p>
      <p>14 Salt Marsh Lane</p>
      <p>Ferncliff 7422</p>
      <p>New Zealand</p>
      <div class="gap"></div>
      <p>Phone +64-(0)3-5207 641</p>
      <p>Cell +64-(0)274-615 203</p>
      <div class="gap"></div>
      <p class="email">Email: redkettlenz@mailbox.example</p>
    </address>

    <p class="website">www.redkettleproductions.example.nz</p>

    <svg class="name-band" width="1200" height="678" viewBox="0 0 1200 678" aria-hidden="true">
      <polygon points="1104,0 1200,0 1200,678 1030,678" fill="var(--band-edge)" stroke="#cfcfcf" stroke-width="1"/>
      <polygon points="1114,0 1200,0 1200,678 1040,678" fill="var(--band-orange)"/>
    </svg>
    <p class="band-name">Toby Harlan</p>
  </div>
</body>
</html>
```